Oil and Gas Construction Company Brochure Design

We're redesigning our company Brochure. The easiest part about this...the layout, content, photos, etc. will follow our newly redesigned website:

www.brivelmarq.com

Thank you very much and please contact me should you have any questions!

Target Market(s)

Engineers, management, and operators in the oil field services

Industry/Entity Type

Oil And Gas

Requirements
Must have
• The same layout as the website, the same content, the same photos (ask me if you need anymore photos or if the layout your chose needs more)
• Also, follow the same color scheme as the website. Follow the same feel/mood as the website. Follow the same text as the website.

```html
<!DOCTYPE html>
<html lang="en">
<head>
<meta charset="utf-8">
<title>Brivelmarq Brochure – Inner Pages</title>
<link href="https://fonts.googleapis.com/css2?family=Roboto:wght@300;400;700&display=swap" rel="stylesheet">
<style>
:root{
  --stage:#2e2e2e;
  --paper:#f4f4f4;
  --panel-a:#cfcfcf;
  --panel-b:#e2e2e2;
  --bar-a:#bdbdbd;
  --bar-b:#e8e8e8;
  --teal:#2a86a6;
  --ink:#1c1c1c;
  --body:#3a3a3a;
  --photo-sky:#8fa7bd;
  --photo-dirt:#a07a5c;
  --photo-steel:#8d9196;
}
*{box-sizing:border-box;margin:0;padding:0}
html,body{width:1200px;height:1200px;overflow:hidden;background:var(--stage);font-family:'Roboto',sans-serif;color:var(--ink)}
.spread{position:absolute;left:205px;width:790px;height:284px;display:flex;box-shadow:0 6px 18px rgba(0,0,0,.5)}
.spread--1{top:172px}.spread--2{top:520px}.spread--3{top:873px}
.page{position:relative;width:395px;height:284px;background:var(--paper)}
.panel{position:absolute;top:18px;left:18px;width:360px;height:248px;background:linear-gradient(100deg,var(--panel-a),var(--panel-b) 60%,var(--panel-a));overflow:hidden}
.page--right .panel{left:17px}
.top-bar{position:absolute;top:0;left:105px;right:0;height:14px;background:linear-gradient(90deg,var(--bar-a),var(--bar-b))}
.top-bar::after{content:"";position:absolute;right:0;top:0;width:26px;height:14px;background:var(--teal)}
.photo{position:absolute}
.photo--yard{background:linear-gradient(180deg,#b9c2c9 0%,#9aa3a8 25%,var(--photo-dirt) 55%,#7a5d48 100%)}
.photo--pipes{background:linear-gradient(90deg,#6d7278,#b5b9bd 45%,var(--photo-steel) 70%,#c9b79f 100%)}
.photo--sky{background:linear-gradient(180deg,#3f6ea8 0%,var(--photo-sky) 45%,#9ea3a7 75%,#7d8287 100%)}
.photo--site{background:linear-gradient(180deg,#b7bcc0 0%,#9c9fa2 30%,var(--photo-dirt) 60%,#8a5e44 100%)}
.bio{position:absolute;width:225px}
.bio__name{font-size:11px;font-weight:400;margin-bottom:2px}
.bio__role{font-size:7.4px;font-weight:300;color:var(--body);margin-bottom:6px}
.bio p{font-size:5.6px;line-height:1.72;font-weight:400;color:var(--body);margin-bottom:6px}
.footer{position:absolute;left:18px;right:18px;bottom:9px;display:flex;justify-content:space-between;align-items:center;font-size:4px;color:#666}
.brand{display:flex;align-items:center;gap:2px;font-size:5px;font-weight:700;color:var(--ink)}
.brand::before{content:"";width:6px;height:6px;border-radius:50%;background:var(--ink)}
.section-title{position:absolute;top:3px;left:5px;font-size:11.5px;font-weight:700}
.emp-intro{position:absolute;left:202px;top:58px;width:150px;font-size:5.8px;line-height:1.75;color:var(--body)}
.emp-lead{position:absolute;left:2px;top:108px;font-size:7px;font-weight:300;color:var(--body)}
.skills{position:absolute;left:6px;top:120px;display:flex;gap:32px;font-size:5.6px;line-height:1.75;color:var(--body);list-style:none}
.skills ul{list-style:disc;padding-left:9px}
.emp-text{position:absolute;left:6px;top:184px;width:350px;font-size:5.6px;line-height:1.75;color:var(--body)}
.emp-text p{margin-bottom:5px}
</style>
</head>
<body>

<section class="spread spread--1">
  <div class="page page--left">
    <div class="panel">
      <div class="top-bar"></div>
      <div class="photo photo--yard" style="left:0;top:26px;width:126px;height:202px" role="img" aria-label="Aerial view of an industrial pipe yard and buildings"></div>
      <div class="bio" style="left:134px;top:26px">
        <h2 class="bio__name">Dale Harwick</h2>
        <div class="bio__role">Vice President of Instrumentation &amp; Electrical</div>
        <p>Mr. Harwick serves as Vice President of Brivelmarq I&amp;E Ltd. He joined Brivelmarq in 2012 and brings 35 years of construction experience in the instrumentation, electrical and automation industry, specializing in the petrochemical, refining, gas processing, power and manufacturing sectors. He is directly responsible for all operational aspects of Brivelmarq I&amp;E Ltd. with a heavy emphasis on safety, quality, management and cost control in all the day to day activities.</p>
        <p>Prior to joining Brivelmarq I&amp;E Ltd., Mr. Harwick served in various roles during a 25 year career at Dunmore Electric Co., Inc. most recently serving as Director of Electrical Services.</p>
        <p>Mr. Harwick holds various technical certifications and is a licensed Master Electrician in the State of Texas.</p>
      </div>
    </div>
    <div class="footer"><span>PAGE # 14</span><span class="brand">BRIVELMARQ</span></div>
  </div>
  <div class="page page--right">
    <div class="panel">
      <div class="top-bar"></div>
      <div class="bio" style="left:10px;top:26px">
        <h2 class="bio__name">Grant Ellory, P.E.</h2>
        <div class="bio__role">Vice President of Business Development</div>
        <p>Mr. Ellory has over 13 years of experience in engineering, construction, operations, project management, and business development. Mr. Ellory's engineering design experience includes: oil &amp; gas gathering and transmission, gas processing, gas conditioning, NGL &amp; condensate stabilization, structural design, large diameter pipelines, wastewater collection, conveyance and pump/lift station design, pipeline assessment, rehabilitation design, and water modeling.</p>
        <p>Prior to joining Brivelmarq, Mr. Ellory served as a Senior Engineer for Pellway Midstream (formerly Ridgecrest Energy). Previously, Mr. Ellory held various positions with Harlow Engineering Solutions, Vantor Group, and Bramley Engineers.</p>
        <p>Mr. Ellory earned a Bachelor of Science in Civil Engineering from Plainsview State University and a Master of Science in Civil Engineering from Plainsview State University. In addition, Mr. Ellory is a Registered Professional Engineer in the State of Texas.</p>
      </div>
      <div class="photo photo--pipes" style="right:0;top:26px;width:126px;height:202px" role="img" aria-label="Bundled conduit pipes curving beside a steel stair tower"></div>
    </div>
    <div class="footer"><span>PAGE # 15</span><span class="brand">BRIVELMARQ</span></div>
  </div>
</section>

<section class="spread spread--2">
  <div class="page page--left">
    <div class="panel">
      <div class="top-bar"></div>
      <div class="photo photo--yard" style="left:0;top:26px;width:126px;height:202px" role="img" aria-label="Aerial view of an industrial pipe yard and buildings"></div>
      <div class="bio" style="left:134px;top:26px">
        <h2 class="bio__name">Ramon Velaro</h2>
        <div class="bio__role">Health, Safety, Environmental and Human Resources Director</div>
        <p>Mr. Velaro joined Brivelmarq Operations in 2013 and brings over 12 years of experience in the Construction Industry, specializing in the refining, oil &amp; gas, nuclear, and mining sectors.</p>
        <p>Prior to joining Brivelmarq Mr. Velaro served as Corporate HSE Manager for Dunmore Industries and was responsible for managing field HSE representatives assigned to various projects. His duties also included providing HSE support for all projects that included implementation, communication and coordination of all environmental, health, and safety programs for the company.</p>
        <p>Mr. Velaro earned a Certificate in Occupational Safety and Health Technology and an Associate of Science in Occupational Safety and Health Technology from Mesa Flats College. In addition, Mr. Velaro holds various certifications in the Construction and General Industries related to HSE including a double CSHO (Certified Safety and Health Official) in both the General and Construction Industries from Lone Range Engineering Extension Service (LREX).</p>
      </div>
    </div>
    <div class="footer"><span>PAGE # 16</span><span class="brand">BRIVELMARQ</span></div>
  </div>
  <div class="page page--right">
    <div class="panel">
      <div class="top-bar"></div>
      <div class="bio" style="left:10px;top:26px">
        <h2 class="bio__name">Neil Castaro</h2>
        <div class="bio__role">Assistant Controller</div>
        <p>Mr. Castaro serves as Assistant Controller of Brivelmarq Operations. He joined Brivelmarq in 2014 and has over 6 years' experience in finance &amp; accounting. He is directly responsible for all accounting aspects of Brivelmarq Constructors, Ltd and Brivelmarq I&amp;E, Ltd including accounts receivable, accounts payable &amp; payroll.</p>
        <p>Prior to joining Brivelmarq, Mr. Castaro served as Commercial Banking Officer and Credit Analyst at Prairie National Bank which specialized in commercial lending to the oil &amp; gas industry.</p>
        <p>Mr. Castaro is also involved in various volunteer roles for a number of non-profit organizations. He has served as President of Willow House Children's Advocacy Center, founding Board Member &amp; Treasurer of Young Professionals of Mesa Flats, Chair for Leadership Mesa Flats and Board Member for Community Fund of Mesa Flats.</p>
        <p>Mr. Castaro earned a Master of Business Administration with a concentration in Finance from Plainsview State University.</p>
      </div>
      <div class="photo photo--pipes" style="right:0;top:26px;width:126px;height:202px" role="img" aria-label="Bundled conduit pipes curving beside a steel stair tower"></div>
    </div>
    <div class="footer"><span>PAGE # 17</span><span class="brand">BRIVELMARQ</span></div>
  </div>
</section>

<section class="spread spread--3">
  <div class="page page--left">
    <div class="panel">
      <div class="top-bar"></div>
      <h2 class="section-title">EMPLOYMENT</h2>
      <div class="photo photo--sky" style="left:0;top:64px;width:185px;height:157px" role="img" aria-label="Gas processing vessel and piping under a blue sky"></div>
      <p class="emp-intro">Brivelmarq Operations is continuously looking for skilled supervision and craft personnel in the industrial service and maintenance fields. Brivelmarq Constructors, LTD is our heavy industrial construction company and Brivelmarq I &amp; E, LTD is our industrial instrumentation and electrical company. We take great pride in providing safe, skilled, multi-craft personnel to all of our industrial clients. Some of the industries which we service include Electric Power Industry, Oil and Gas Industry, and the Petrochemical Industry.</p>
    </div>
    <div class="footer"><span>PAGE # 18</span><span class="brand">BRIVELMARQ</span></div>
  </div>
  <div class="page page--right">
    <div class="panel">
      <div class="top-bar"></div>
      <div class="photo photo--site" style="left:0;top:0;width:360px;height:102px" role="img" aria-label="Construction site with rebar foundation pit and steel pipe racks"></div>
      <p class="emp-lead">Brivelmarq Operations is interested in speaking with you if you have experience or training in the following fields:</p>
      <div class="skills">
        <ul><li>General Construction</li><li>Concrete Construction</li><li>Equipment Erection and Assembly</li><li>Equipment Operating</li><li>High Pressure Testing</li><li>Pipe Fitting</li></ul>
        <ul><li>Sandblasting and Painting</li><li>Structural Steel Erection</li><li>Welding</li><li>Instrument and Electrical Construction</li><li>Field Office Management</li><li>Estimating</li></ul>
        <ul><li>QA/QC</li><li>Project Management</li><li>Health, Safety &amp; Environmental</li><li>Accounts Receivable</li><li>Accounts Payable</li><li>Payroll</li></ul>
      </div>
      <div class="emp-text">
        <p>We recognize that our employees are our most valuable asset. To be successful, Brivelmarq Operations must be a rewarding place to work. We promote opportunity and provide encouragement to help our people reach their full potential. We believe in mutual respect and know it provides the foundation for our success. We work with our employees as a team and together we will succeed.</p>
        <p>To apply, use the Contact form or call us at (555) 014-2760 to request a job application.<br>You may also email your resume to careers@brivelmarq.com.</p>
      </div>
    </div>
    <div class="footer"><span>PAGE # 19</span><span class="brand">BRIVELMARQ</span></div>
  </div>
</section>

</body>
</html>
```